Dorvell landscape website

Our company is called Dorvell Landscape, Inc. We are located in Oak Bluffs, Martha's Vineyard Island, MA. We are a design construction maintenance firm offering a wide variety of services. We need to build a website for our Landscape, Construction, and Maintenance Company. The ability to interchange photos in many locations. 6-7 Tabs for individualized services. Ability to change and alter text. Use of our logo to increase branding. Modern, clean, simplified backgrounds are appealing. Possibly black background to allow the colors of flowers and logos to pop. Simplicity in management is of importance! The final design should lend itself to an upscale marketplace.
Updates

Dear Designers, Please be advised that the web design needs coding as well. Coding will not be charged on top of whatever investment and must be inclusive in the package. In short, you will not ask the client for more funds. -ArtFolio Admin (Tomas Ferreira)

Target Market(s)

These are second homeowners. estate type properties. upscale clientele.

Industry/Entity Type

Construction

Requirements
Must have
• multiple tabs 6-7 to be able to highlight services. space for text and photos/albums. easy to navigate.
Should not have
• cheesy gimmicky cheap type feel

```html
<!DOCTYPE html>
<html lang="en">
<head>
<meta charset="utf-8">
<title>Dorvell Landscape</title>
<link rel="stylesheet" href="https://fonts.googleapis.com/css2?family=Pathway+Gothic+One&family=Roboto+Condensed:wght@400;700&family=Arimo:ital@0;1&family=Libre+Baskerville:ital@1&display=swap">
<style>
:root{
  --bg:#0c0c0c;
  --header:#121212;
  --section:#101010;
  --footer:#060606;
  --bar:#141414;
  --white:#ffffff;
  --muted:#9a9a9a;
  --dim:#7a7a7a;
  --orange:#f2a21c;
  --red:#e0301e;
  --line:#3a3a3a;
  --green:#2f7a2a;
  --icon:#6e6e6e;
}
*{margin:0;padding:0;box-sizing:border-box}
html,body{width:812px;height:1200px;overflow:hidden;background:var(--bg)}
body{position:relative;font-family:"Arimo",Arial,sans-serif;color:var(--white)}
.abs{position:absolute}

.hero{left:0;top:0;width:812px;height:422px;
  background:
    radial-gradient(ellipse 230px 80px at 560px 230px,rgba(150,150,155,.55),rgba(150,150,155,0) 100%),
    radial-gradient(ellipse 300px 90px at 640px 310px,rgba(70,110,40,.55),rgba(70,110,40,0) 100%),
    linear-gradient(180deg,#1f2a1a 0%,#2e3d26 22%,#4a5548 45%,#3f5a2c 66%,#24331a 82%,#141a0f 100%);}
.hero-shade{left:0;top:290px;width:812px;height:132px;background:linear-gradient(180deg,rgba(0,0,0,0),rgba(0,0,0,.72))}
.header{left:0;top:0;width:812px;height:54px;background:var(--header)}

.brand-circle{left:117px;top:8px;width:97px;height:97px;border-radius:50%;background:var(--green);border:3px solid #fff}
.brand-name{left:117px;top:46px;width:97px;text-align:center;font-family:"Roboto Condensed",sans-serif;font-weight:700;font-size:15px;color:#fff;letter-spacing:1px}
.tagline{left:112px;top:111px;font-family:"Libre Baskerville",serif;font-style:italic;font-size:7.5px;line-height:13px;color:#e6e6e6}

.nav a{position:absolute;top:22px;font-family:"Roboto Condensed",sans-serif;font-size:9.5px;color:#fff;text-decoration:none;text-transform:uppercase}
.login{left:646px;top:17px;width:50px;height:19px;border:1px solid #777;font-family:"Roboto Condensed",sans-serif;font-size:7.5px;line-height:17px;padding-left:11px;color:#fff}
.login svg{position:absolute;right:8px;top:7px}

.hero-title{left:117px;top:213px;font-family:"Pathway Gothic One",sans-serif;font-weight:400;font-size:26px;line-height:30px;font-variant:small-caps;color:#fff}
.slide-arrow{top:186px}

.service{width:155px;top:317px}
.service h3{font-family:"Roboto Condensed",sans-serif;font-weight:400;font-size:12px;color:var(--orange);padding-bottom:5px;border-bottom:1px solid #ddd}
.service .copytext{margin-top:8px;font-size:7px;line-height:13.4px;color:#f0f0f0}
.service .more{margin-top:4px;font-size:7px;color:var(--red)}

.welcome{left:0;top:422px;width:812px;height:188px;background:var(--section)}
.section-title{width:812px;left:0;text-align:center;font-family:"Pathway Gothic One",sans-serif;font-weight:400;font-size:38px;color:#fff;letter-spacing:1px}
.section-text{left:140px;width:532px;text-align:center;font-size:6.8px;line-height:14.4px}

.gallery{left:0;top:610px;width:812px;height:396px;
  background:
    radial-gradient(ellipse 260px 70px at 330px 118px,rgba(230,140,40,.55),rgba(230,140,40,0) 100%),
    radial-gradient(ellipse 170px 110px at 720px 60px,rgba(40,26,16,.85),rgba(40,26,16,0) 100%),
    linear-gradient(180deg,#5a3a16 0%,#7a4818 16%,#6a3c14 26%,#3a2412 32%,#2e1e12 55%,#3a2616 78%,#241810 100%);}
.grid{left:116px;top:740px;width:580px;height:215px;display:grid;grid-template-columns:repeat(4,1fr);grid-template-rows:repeat(2,1fr);gap:1px}
.grid div{width:100%;height:100%}

.footer{left:0;top:1006px;width:812px;height:154px;background:var(--footer)}
.foot-links{width:84px;list-style:none}
.foot-links li{height:20.3px;border-bottom:1px solid var(--line);font-size:6px;color:var(--dim);padding-top:4px}
.foot-head{font-family:"Roboto Condensed",sans-serif;font-weight:400;font-size:9px;color:#fff}
.news-text{left:388px;top:1063px;width:150px;font-size:6.5px;line-height:13.4px;color:var(--dim)}
.posted{left:386px;top:1122px;font-size:6px;font-style:italic;color:var(--red)}
.field{left:561px;width:131px;height:14px;border:1px solid #555;font-size:6px;color:#aaa;padding:3px 7px}
.subscribe{left:641px;top:1102px;font-family:"Roboto Condensed",sans-serif;font-size:8px;color:var(--red)}

.bar{left:0;top:1160px;width:812px;height:40px;background:var(--bar)}
.copy{left:116px;top:1176px;font-size:6px;color:var(--muted)}
.social{left:546px;top:1175px;display:flex;gap:15px}
.social span{width:8px;height:8px;border:1px solid var(--icon);border-radius:2px}
</style>
</head>
<body>
<div class="abs hero" role="img" aria-label="Photo of a grey shingled cottage among tall trees with a landscaped lawn and shrubs"></div>
<div class="abs hero-shade"></div>
<div class="abs header"></div>

<div class="abs brand-circle"></div>
<div class="abs brand-name">Dorvell</div>
<p class="abs tagline">Complete landscape construction<br>and design on Martha's Vineyard</p>

<nav class="nav">
  <a style="left:270px">Home</a>
  <a style="left:335px">About us</a>
  <a style="left:416px">Services</a>
  <a style="left:495px">Property</a>
  <a style="left:578px">Contact us</a>
</nav>
<div class="abs login">LOGIN<svg width="6" height="4"><path d="M0 0h6L3 3z" fill="#fff"/></svg></div>

<svg class="abs slide-arrow" style="left:42px" width="16" height="52"><path d="M14 1L2 26l12 25" fill="none" stroke="#aaa" stroke-width="1"/></svg>
<svg class="abs slide-arrow" style="left:756px" width="16" height="52"><path d="M2 1l12 25L2 51" fill="none" stroke="#aaa" stroke-width="1"/></svg>

<h1 class="abs hero-title">Complete landscape construction<br>and design on Martha's Vineyard</h1>
<svg class="abs" style="left:364px;top:218px" width="22" height="54"><path d="M2 2l9 25-9 25M10 2l9 25-9 25" fill="none" stroke="#fff" stroke-width="2"/></svg>

<section class="abs service" style="left:116px">
  <h3>LANDSCAPE</h3>
  <p class="copytext">Lorem Ipsum is simply dummy text of the printing and typesetting industry. Lorem Ipsum has been the industry's standard dummy text...</p>
  <p class="more">Click here for more info &raquo;</p>
</section>
<section class="abs service" style="left:319px">
  <h3>CONSTRUCTION</h3>
  <p class="copytext">Lorem Ipsum is simply dummy text of the printing and typesetting industry. Lorem Ipsum has been the industry's standard dummy text...</p>
  <p class="more">Click here for more info &raquo;</p>
</section>
<section class="abs service" style="left:522px">
  <h3>MAINTENANCE</h3>
  <p class="copytext">Lorem Ipsum is simply dummy text of the printing and typesetting industry. Lorem Ipsum has been the industry's standard dummy text...</p>
  <p class="more">Click here for more info &raquo;</p>
</section>

<div class="abs welcome"></div>
<h2 class="abs section-title" style="top:458px">WELCOME TO DORVELL LANDSCAPE</h2>
<p class="abs section-text" style="top:512px;color:var(--muted)">Lorem Ipsum is simply dummy text of the printing and typesetting industry. Lorem Ipsum has been the industry's standard dummy text ever since the 1500s, when an unknown printer took a galley of type and scrambled it to make a type specimen book. It has survived not only five centuries, but also the leap into electronic typesetting,remaining essentially unchanged. It was popularised in the 1960s with the release of Letraset sheets containing Lorem Ipsum passages, and more recently with desktop publishing software like Aldus PageMaker including versions of Lorem Ipsum.</p>

<div class="abs gallery" role="img" aria-label="Sunset over a dark sea framed by a rock arch"></div>
<h2 class="abs section-title" style="top:644px">PHOTO GALLERY</h2>
<p class="abs section-text" style="top:687px;color:#fff">Lorem Ipsum is simply dummy text of the printing and typesetting industry. Lorem Ipsum has been the industry's standard dummy text ever since the 1500s, when an unknown printer took a galley of type and scrambled it to make a type specimen book.</p>

<div class="abs grid">
  <div role="img" aria-label="Bare trees on a cleared lot" style="background:linear-gradient(180deg,#cfcbc4 0%,#8a7a66 45%,#6e5a44 100%)"></div>
  <div role="img" aria-label="Timber shed under construction" style="background:linear-gradient(180deg,#4a3428 0%,#b47a4e 45%,#d09868 70%,#6a4a34 100%)"></div>
  <div role="img" aria-label="Crew standing in front of an aircraft" style="background:linear-gradient(180deg,#c4c8cc 0%,#a8acb0 40%,#dfe2e4 60%,#4e5256 100%)"></div>
  <div role="img" aria-label="Coastal cliffs and beach" style="background:linear-gradient(180deg,#4a7cb4 0%,#90b0d0 40%,#d8e0e6 58%,#7a6a50 100%)"></div>
  <div role="img" aria-label="Grey cottage with green lawn" style="background:linear-gradient(180deg,#e6eaec 0%,#4e7a3a 35%,#8a96a2 55%,#3e6a2c 100%)"></div>
  <div role="img" aria-label="Worker watering a hillside" style="background:linear-gradient(180deg,#b0b8b4 0%,#5a7a48 40%,#3e5430 65%,#a89474 100%)"></div>
  <div role="img" aria-label="House with a long driveway" style="background:linear-gradient(180deg,#d0d4d8 0%,#6a5a48 35%,#4e6a32 60%,#b0a48c 100%)"></div>
  <div role="img" aria-label="Flower bed on a stone wall" style="background:linear-gradient(180deg,#d6dde4 0%,#4e7a34 30%,#9a8e80 50%,#c8c4bc 70%,#e0ddd8 100%)"></div>
</div>

<footer>
<div class="abs footer"></div>
<ul class="abs foot-links" style="left:122px;top:1040px">
  <li>Home</li><li>About us</li><li>Services</li><li>Property</li><li>Contact us</li>
</ul>
<ul class="abs foot-links" style="left:255px;top:1040px">
  <li>Terms &amp; Conditions</li><li>Privacy Policy</li><li>Disclaimer</li><li>Sitemap</li>
</ul>
<h4 class="abs foot-head" style="left:386px;top:1041px">LATEST NEWS</h4>
<svg class="abs" style="left:512px;top:1041px" width="16" height="8"><path d="M4 1L1 4l3 3M12 1l3 3-3 3" fill="none" stroke="#fff" stroke-width="1.3"/></svg>
<p class="abs news-text">Lorem Ipsum is simply dummy text of the printing and typesetting industry. Lorem Ipsum has been the industry's standard dummy text ever since the 1500s, when an unknown...</p>
<p class="abs posted">Posted on 25 Dec 2014</p>
<h4 class="abs foot-head" style="left:561px;top:1041px">NEWSLETTER SIGNUP</h4>
<div class="abs field" style="top:1060px">Name :</div>
<div class="abs field" style="top:1080px">Email :</div>
<div class="abs subscribe">SUBSCRIBE &raquo;</div>
</footer>

<div class="abs bar"></div>
<p class="abs copy">&copy; 2014. Dorvell Landscape. All rights reserved.</p>
<div class="abs social" aria-label="Social links"><span></span><span></span><span></span><span></span><span></span><span></span><span></span></div>
</body>
</html>
```